Professional law firm looking for new professional and eye-catching business card design

Law firm in need of new business card design using existing firm logo and firm colors on thick card stock. Firm colors are navy blue, cyan blue, and gray. Please use firm's logo either on the back of the card or on the front and back. I am looking for something eye-catching and resonating but also professional.

Target Market(s)

Law firm growth by attracting clients with professional, creative, and attractive business cards.

Industry/Entity Type

Legal/Law Firm

Contact Information for Business Card

Name: Derek T. Halloway, Esq., Address: 517 E. Quintley Blvd., P.O. Box 641, Tavares, FL 32790, Phone numbers: (352) 555-0187 Office, (352) 555-0142 Fax, email address: DerekH@hqlegalfx.com, website: www.HQLegalFX.com

Font styles to use
Other font styles liked:
• Font as close as possible to matching law firm logo.

Requirements
Must have
• Must have business card details and law firm logo with law firm colors.

```html
<!DOCTYPE html>
<html lang="en">
<head>
<meta charset="utf-8">
<title>HQ Legal — Business Card</title>
<link rel="stylesheet" href="https://fonts.googleapis.com/css2?family=Josefin+Sans:wght@400;600&family=Roboto:wght@400;500&display=swap">
<style>
  :root {
    --navy: #07072e;
    --navy-stripe: #0b0b38;
    --cyan: #2fb4ec;
    --cyan-dark: #1a94cc;
    --gray: #cfd0d4;
    --ink: #1d1d2a;
    --page: #ffffff;
  }
  * { box-sizing: border-box; margin: 0; padding: 0; }
  html, body { width: 1200px; height: 1200px; overflow: hidden; background: var(--page); }
  .sheet {
    width: 1200px; height: 1200px;
    display: flex; align-items: center; justify-content: center; gap: 40px;
  }
  .card {
    position: relative; width: 560px; height: 326px; overflow: hidden;
    background: var(--navy) repeating-linear-gradient(90deg, var(--navy) 0 6px, var(--navy-stripe) 6px 8px);
  }
  .edge-tab {
    position: absolute; top: 34px; height: 258px; width: 18px;
    background: linear-gradient(90deg, var(--cyan-dark), var(--cyan));
  }
  .edge-tab--left { left: 0; }
  .edge-tab--right { right: 0; }

  .firm-mark {
    display: flex; align-items: center; gap: 10px;
    font-family: "Josefin Sans", sans-serif; font-weight: 600;
    color: var(--cyan); font-size: 40px; letter-spacing: 1px;
  }
  .firm-mark__dot { width: 14px; height: 14px; border-radius: 50%; background: var(--cyan); }

  .card--front .firm-mark { position: absolute; left: 0; right: 0; top: 128px; justify-content: center; }
  .card--front .website {
    position: absolute; left: 0; right: 0; top: 254px; text-align: center;
    font-family: "Roboto", sans-serif; font-weight: 500; font-size: 14px; color: var(--cyan);
  }

  .icon-rail {
    position: absolute; left: 0; top: 34px; width: 60px; height: 258px;
    background: linear-gradient(90deg, var(--cyan-dark), var(--cyan));
  }
  .icon { position: absolute; left: 19px; width: 22px; height: 22px; z-index: 2; }
  .icon--person { top: 64px; }
  .icon--phone { top: 124px; }
  .icon--pin { top: 185px; }
  .icon--mail { top: 236px; }
  .details {
    position: absolute; left: 60px; top: 0; width: 242px; height: 326px;
    background: var(--gray); color: var(--ink);
    font-family: "Roboto", sans-serif;
  }
  .details__name {
    position: absolute; left: 12px; top: 70px; white-space: nowrap;
    font-family: "Josefin Sans", sans-serif; font-weight: 400; font-size: 15px;
    letter-spacing: 0.2px; text-transform: uppercase;
  }
  .details__block { position: absolute; left: 12px; font-size: 10px; line-height: 16px; white-space: nowrap; }
  .details__phones { top: 119px; }
  .details__address { top: 180px; }
  .details__email { top: 241px; }
  .card--back .firm-mark { position: absolute; left: 302px; right: 0; top: 140px; justify-content: center; font-size: 34px; }
</style>
</head>
<body>
<main class="sheet">
  <section class="card card--front" aria-label="Card front">
    <div class="edge-tab edge-tab--left"></div>
    <div class="edge-tab edge-tab--right"></div>
    <div class="firm-mark"><span class="firm-mark__dot"></span>HQ Legal</div>
    <p class="website">www.HQLegalFX.com</p>
  </section>

  <section class="card card--back" aria-label="Card back">
    <div class="icon-rail"></div>
    <svg class="icon icon--person" viewBox="0 0 24 24" aria-hidden="true"><circle cx="12" cy="8" r="5" fill="#07072e"/><path d="M3 22c0-5 4-8 9-8s9 3 9 8z" fill="#07072e"/></svg>
    <svg class="icon icon--phone" viewBox="0 0 24 24" aria-hidden="true"><path d="M6.6 10.8c1.4 2.8 3.8 5.1 6.6 6.6l2.2-2.2c.3-.3.7-.4 1-.2 1.1.4 2.3.6 3.6.6.6 0 1 .4 1 1V20c0 .6-.4 1-1 1C10.6 21 3 13.4 3 4c0-.6.4-1 1-1h3.5c.6 0 1 .4 1 1 0 1.3.2 2.5.6 3.6.1.3 0 .7-.2 1z" fill="#07072e"/></svg>
    <svg class="icon icon--pin" viewBox="0 0 24 24" aria-hidden="true"><path d="M12 2a7 7 0 0 0-7 7c0 5 7 13 7 13s7-8 7-13a7 7 0 0 0-7-7zm0 9.5A2.5 2.5 0 1 1 12 6.5a2.5 2.5 0 0 1 0 5z" fill="#07072e"/></svg>
    <svg class="icon icon--mail" viewBox="0 0 24 24" aria-hidden="true"><rect x="2" y="5" width="20" height="14" fill="#07072e"/><path d="M2 5l10 8 10-8" fill="none" stroke="#2fb4ec" stroke-width="1.5"/></svg>

    <div class="details">
      <h1 class="details__name">Derek T. Halloway, Esq.</h1>
      <p class="details__block details__phones">(352) 555-0187 Office<br>(352) 555-0142 Fax</p>
      <p class="details__block details__address">517 E. Quintley Blvd., P.O. Box 641,<br>Tavares, FL 32790</p>
      <p class="details__block details__email">DerekH@hqlegalfx.com</p>
    </div>
    <div class="firm-mark"><span class="firm-mark__dot"></span>HQ Legal</div>
  </section>
</main>
</body>
</html>
```